I am looking for a flyer design for my upcoming symposium. Here are the details for the flyer and pictures of speakers are attached.

Name of Symposium: Lattice and Pathway Biosciences Symposium, Sponsored by the Corvale Chromatin Institute and the Department of Bioengineering
Date: January 8, 2018
Location: Havergill Auditorium, Tarnby Center for Applied Discovery, 2175 Orchard Terrace Ave, Philadelphia, PA 19127

Reception to follow after the symposium.

Also, please add - Register and upload abstracts for the symposium at www.qzvmrk.com. Registration and abstract submission closes on January 4, 2018.

Keynote Speaker:
Marthe Quillon, Ph.D.
NTVO Director General; Professor, Lyceum of Norvane; Director, Genetics and Developmental Biology at Institut Bramoux
Lyceum of Norvane, NTVO, Institut Bramoux
"Title of talk TBA."

Speakers:
Lena Drewcott, Ph.D.
Assistant Professor of Cell and Developmental Biology
Halvering State University, HMCS
"Title of talk TBA."

Paul Marden, Ph.D.
Assistant Professor of Genetics
"Title of talk TBA."

Ilse Varga, Ph.D.
Professor, Ostrander University
Otto Wenzlau Center for Molecular Medicine
"Title of talk TBA."

Jun Hao, Ph.D.
Professor of Cellular and Molecular Medicine
Coastal Meridian University
"Title of talk TBA."

Wei Lun, Ph.D.
Associate Professor of Pediatrics
The Youth Medical Pavilion of Philadelphia
"Spatial genome re-organization between fetal and adult hematopoietic stem cells."

Mei Zhou, Ph.D.
Professor, Department of Genetics
Ellsworth Medical School
"Title of talk TBA."

```html
<!DOCTYPE html>
<html lang="en">
<head>
<meta charset="utf-8">
<title>Lattice and Pathway Biosciences Symposium</title>
<link rel="stylesheet" href="https://fonts.googleapis.com/css2?family=Montserrat:wght@600;700&family=Poppins:wght@400;500;600&display=swap">
<style>
  :root {
    --red: #ee2c36;
    --red-dark: #b3151f;
    --red-deep: #8f0f17;
    --blush: #fbd6d7;
    --white: #ffffff;
    --ink: #111111;
    --navy: #1d2a6b;
    --frame: #3a3a3a;
  }
  * { box-sizing: border-box; margin: 0; padding: 0; }
  html, body { width: 849px; height: 1200px; overflow: hidden; background: var(--white); }
  .flyer {
    position: relative; width: 849px; height: 1200px; overflow: hidden;
    font-family: "Poppins", Arial, sans-serif; color: var(--ink);
    background: linear-gradient(to bottom, var(--white) 0, var(--white) 260px, var(--blush) 270px, var(--white) 420px);
  }
  .header-band { position: absolute; left: 0; top: 0; width: 849px; height: 300px; }
  .title {
    position: absolute; left: 0; right: 0; top: 32px; text-align: center;
    font-family: "Montserrat", Arial, sans-serif; font-weight: 600;
    font-size: 112px; line-height: 1; letter-spacing: 1px; color: var(--white);
  }
  .subtitle {
    position: absolute; left: 0; right: 0; top: 156px; text-align: center;
    font-weight: 500; font-size: 20.5px; line-height: 28px; color: var(--white);
  }
  .date-ribbon { position: absolute; left: 188px; top: 240px; width: 466px; height: 72px; }
  .date-text {
    position: absolute; left: 0; right: 0; top: 259px; text-align: center;
    font-weight: 600; font-size: 31px; letter-spacing: 0.5px; color: var(--white);
  }
  .register { position: absolute; left: 0; right: 0; top: 338px; text-align: center; color: var(--red); }
  .register .line { font-weight: 500; font-size: 23px; line-height: 30px; }
  .register .url { font-family: "Montserrat", Arial, sans-serif; font-weight: 700; font-size: 37px; line-height: 36px; letter-spacing: 3px; }
  .register .deadline { font-family: "Montserrat", Arial, sans-serif; font-weight: 700; font-size: 44px; line-height: 50px; }

  .speaker { position: absolute; width: 420px; height: 130px; }
  .speaker .photo {
    position: absolute; left: 0; top: 0; width: 112px; height: 128px;
    border: 2px solid var(--frame); border-radius: 6px;
  }
  .speaker .bio { position: absolute; left: 123px; top: 8px; width: 300px; font-size: 12.3px; line-height: 16.6px; }
  .speaker .bio.plain { top: 24px; }
  .speaker .role { font-size: 12.3px; }
  .speaker .name { color: var(--red); font-weight: 500; font-size: 21px; line-height: 24px; letter-spacing: -0.2px; }
  .speaker .talk { font-style: normal; }

  .institute-name {
    position: absolute; left: 492px; top: 962px; width: 270px; display: flex; align-items: center; gap: 12px;
    font-weight: 600; font-size: 20px; line-height: 24px; color: var(--navy);
  }
  .institute-name .dot { flex: none; width: 34px; height: 34px; border-radius: 50%; background: var(--navy); }
  .engineering-name {
    position: absolute; left: 52px; top: 1108px; display: flex; align-items: center; gap: 12px;
    font-weight: 600; font-size: 22px; color: var(--navy);
  }
  .engineering-name .mark { width: 40px; height: 40px; background: var(--navy); }

  .venue-band { position: absolute; left: 0; top: 1077px; width: 849px; height: 123px; }
  .venue {
    position: absolute; right: 36px; top: 1098px; text-align: right;
    font-weight: 500; font-size: 18.5px; line-height: 24px; color: var(--white);
  }
</style>
</head>
<body>
<main class="flyer">
  <svg class="header-band" viewBox="0 0 849 300" aria-hidden="true">
    <path d="M0 0 H849 V284 Q424 222 0 284 Z" fill="var(--red)"/>
  </svg>
  <h1 class="title">SYMPOSIUM</h1>
  <p class="subtitle">Lattice and Pathway Biosciences Symposium, Sponsored by the<br>Corvale Chromatin Institute and the Department of Bioengineering</p>

  <svg class="date-ribbon" viewBox="0 0 466 72" aria-hidden="true">
    <polygon points="0,40 44,2 44,60" fill="var(--red-deep)"/>
    <polygon points="466,40 422,2 422,60" fill="var(--red-deep)"/>
    <rect x="42" y="0" width="382" height="70" rx="10" fill="var(--red-dark)"/>
  </svg>
  <p class="date-text">JANUARY 8, 2018</p>

  <section class="register">
    <p class="line">Register and upload abstracts for the symposium at</p>
    <p class="url">www.qzvmrk.com</p>
    <p class="line">Registration and abstract submission closes on</p>
    <p class="deadline">JANUARY 4, 2018.</p>
  </section>

  <article class="speaker" style="left:19px; top:503px;">
    <div class="photo" role="img" aria-label="Portrait of keynote speaker Marthe Quillon" style="background:linear-gradient(160deg,#8a6a58,#c9a894 55%,#6e5546);"></div>
    <div class="bio">
      <p class="role">Keynote Speaker:</p>
      <h2 class="name">Marthe Quillon, Ph.D.</h2>
      <p>NTVO Director General; Professor, Lyceum of Norvane;<br>Director, Genetics and Developmental Biology at Ins.<br>Lyceum of Norvane, NTVO, Institut Bramoux<br>"Title of talk TBA."</p>
    </div>
  </article>

  <article class="speaker" style="left:19px; top:643px;">
    <div class="photo" role="img" aria-label="Portrait of speaker Lena Drewcott" style="background:linear-gradient(160deg,#5a4036,#d8b5a0 55%,#7b6a5e);"></div>
    <div class="bio">
      <p class="role">Speakers:</p>
      <h2 class="name">Lena Drewcott, Ph.D.</h2>
      <p>Assistant Professor of Cell and<br>Developmental Biology<br>Halvering State University, HMCS<br>"Title of talk TBA."</p>
    </div>
  </article>

  <article class="speaker" style="left:19px; top:783px;">
    <div class="photo" role="img" aria-label="Portrait of speaker Jun Hao" style="background:linear-gradient(160deg,#dfe3e6,#d8b08e 55%,#9aa4ad);"></div>
    <div class="bio plain">
      <h2 class="name">Jun Hao, Ph.D.</h2>
      <p>Professor of Cellular and Molecular<br>Medicine<br>Coastal Meridian University<br>"Title of talk TBA."</p>
    </div>
  </article>

  <article class="speaker" style="left:19px; top:923px;">
    <div class="photo" role="img" aria-label="Portrait of speaker Wei Lun" style="background:linear-gradient(160deg,#b8c7d4,#d9b394 50%,#6f95c4);"></div>
    <div class="bio plain">
      <h2 class="name">Wei Lun, Ph.D.</h2>
      <p>Associate Professor of Pediatrics<br>The Youth Medical Pavilion of Philadelphia<br>"Spatial genome re-organization between<br>fetal and adult hematopoietic stem cells."</p>
    </div>
  </article>

  <article class="speaker" style="left:467px; top:503px;">
    <div class="photo" role="img" aria-label="Portrait of speaker Paul Marden" style="background:linear-gradient(160deg,#7a2f2a,#d9a88a 55%,#e9e4df);"></div>
    <div class="bio plain">
      <h2 class="name">Paul Marden, Ph.D.</h2>
      <p>Assistant Professor of Genetics<br>Halvering State University, HMCS<br>"Title of talk TBA."</p>
    </div>
  </article>

  <article class="speaker" style="left:467px; top:643px;">
    <div class="photo" role="img" aria-label="Portrait of speaker Ilse Varga" style="background:linear-gradient(160deg,#2b2422,#c9a48e 55%,#3b3431);"></div>
    <div class="bio plain">
      <h2 class="name">Ilse Varga, Ph.D.</h2>
      <p>Professor, Ostrander University<br>Otto Wenzlau Center for Molecular<br>Medicine<br>"Title of talk TBA."</p>
    </div>
  </article>

  <article class="speaker" style="left:467px; top:783px;">
    <div class="photo" role="img" aria-label="Portrait of speaker Mei Zhou" style="background:linear-gradient(160deg,#4d5a3c,#d6b49c 55%,#6d6a5a);"></div>
    <div class="bio plain">
      <h2 class="name">Mei Zhou, Ph.D.</h2>
      <p>Professor, Department of Genetics<br>Ellsworth Medical School<br>"Title of talk TBA."</p>
    </div>
  </article>

  <div class="institute-name"><span class="dot"></span><span>Corvale Chromatin Institute</span></div>
  <div class="engineering-name"><span class="mark"></span><span>Halvering Engineering</span></div>

  <svg class="venue-band" viewBox="0 0 849 123" aria-hidden="true">
    <polygon points="402,0 849,0 849,123 302,123" fill="var(--red)"/>
  </svg>
  <address class="venue" style="font-style:normal;">Havergill Auditorium,<br>Tarnby Center for Applied Discovery,<br>2175 Orchard Terrace Ave, Philadelphia, PA 19127</address>
</main>
</body>
</html>
```